Business Card & Word Docs from existing Logo

We need a business card with typical information plus layout to include electrical contractors license number, VONEL license and KMP license. We would like a word document layout for a proposal document, opening page with logo and design basic information; proposal to and proposal from and project name and number. Small basic single page letter for general documents. Email signature with logo.

We are an electrical, refrigeration and automation contractor. We work with reducing energy consumption for our customers and complex process solutions in electrical, refrigeration and automation.

Reason: Final changes/ revisions to designs.

Target Market(s)

Industrial and commercial businesses that require more than your average contractor.

Industry/Entity Type

Electrical

Requirements
Must have
• Propsal document must have a full opening page.

```html
<!DOCTYPE html>
<html lang="en">
<head>
<meta charset="utf-8">
<title>Kelvara Contracting – Business Card</title>
<link href="https://fonts.googleapis.com/css2?family=Arimo:wght@400;700&display=swap" rel="stylesheet">
<style>
  :root {
    --page-bg: #ffffff;
    --card-bg: #ffffff;
    --ink: #1b1b1b;
    --brand-blue: #2f7fb5;
    --brand-navy: #1d3f6e;
    --wash-blue: #6f9cc2;
    --wash-grey: #b4bfca;
    --wash-green: #c9dfc0;
    --city-dark: #1e1a1a;
    --city-grey: #9a9a9a;
  }
  * { margin: 0; padding: 0; box-sizing: border-box; }
  html, body {
    width: 1200px; height: 900px; overflow: hidden;
    background: var(--page-bg);
    font-family: "Arimo", Arial, sans-serif;
    color: var(--ink);
  }
  .canvas { position: relative; width: 1200px; height: 900px; }

  .card {
    position: absolute; top: 186px;
    width: 319px; height: 511px;
    background: var(--card-bg);
    overflow: hidden;
    outline: 1px solid #e4e4e4;
  }
  .card--front { left: 136px; }
  .card--back  { left: 741px; }

  /* Front: soft blue wash fading downwards */
  .front-wash {
    position: absolute; inset: 0 0 auto 0; height: 440px;
    background: linear-gradient(180deg, var(--wash-blue) 0%, rgba(160,185,205,.7) 35%, rgba(220,228,235,.4) 70%, rgba(255,255,255,0) 100%);
  }
  .front-brand {
    position: absolute; left: 20px; bottom: 26px;
    display: flex; align-items: center; gap: 9px;
  }
  .front-brand__dot {
    width: 32px; height: 32px; border-radius: 50%;
    background: var(--brand-blue);
  }
  .front-brand__name {
    font-size: 17px; font-weight: 700; letter-spacing: .5px;
    color: var(--brand-navy);
  }

  /* Back: soft diagonal grey-green wash */
  .back-wash {
    position: absolute; inset: 0;
    background: linear-gradient(200deg, var(--wash-grey) 0%, var(--wash-green) 30%, rgba(225,230,235,.7) 60%, rgba(245,246,247,.5) 100%);
  }
  .contact { position: absolute; inset: 0; }
  .contact__name {
    position: absolute; right: 17px; top: 42px;
    font-size: 28px; font-weight: 700; white-space: nowrap;
  }
  .contact__role {
    position: absolute; right: 17px; top: 76px;
    font-size: 15px; white-space: nowrap;
  }
  .contact__address {
    position: absolute; left: 13px; top: 121px;
    font-size: 16px; white-space: nowrap;
  }
  .contact__lines {
    position: absolute; left: 15px; top: 206px;
    list-style: none; font-size: 16px; line-height: 21px; white-space: nowrap;
  }
  .contact__lines .label { display: inline-block; width: 28px; }
  .contact__licences {
    position: absolute; left: 15px; top: 328px;
    list-style: none; font-size: 16px; line-height: 21px; white-space: nowrap;
  }
  .skyline {
    position: absolute; left: 0; right: 0; bottom: 0; height: 58px;
    background: linear-gradient(180deg, var(--city-grey), var(--city-dark));
  }
</style>
</head>
<body>
<main class="canvas">
  <section class="card card--front" aria-label="Card front">
    <div class="front-wash" role="img" aria-label="Vertical blue, green and grey stripe pattern fading down the card"></div>
    <div class="front-brand">
      <span class="front-brand__dot"></span>
      <span class="front-brand__name">KELVARA CONTRACTING</span>
    </div>
  </section>

  <section class="card card--back" aria-label="Card back">
    <div class="back-wash" role="img" aria-label="Diagonal grey and green stripe pattern"></div>
    <div class="contact">
      <h1 class="contact__name">Tom Barlow</h1>
      <p class="contact__role">Director</p>
      <p class="contact__address">PO Box 5678 Kurrin Queensland 4999</p>
      <ul class="contact__lines">
        <li><span class="label">T :</span>07 5550 1820</li>
        <li><span class="label">F :</span>07 5550 1821</li>
        <li><span class="label">M:</span>0400 555 319</li>
        <li>Email: tom@kelvara.com.au</li>
        <li>Web: www.kelvara.com.au</li>
      </ul>
      <ul class="contact__licences">
        <li>Electrical Contractors License 12345</li>
        <li>KMP 1234567</li>
        <li>VONEL AA12345</li>
      </ul>
    </div>
    <div class="skyline" role="img" aria-label="City skyline silhouette in black and grey"></div>
  </section>
</main>
</body>
</html>
```